Upscale business cards needed for Board of Directors

We need professional business cards created for members of our family business Board of Directors. We would like these relatively simple and straightforward, but also with a unique element to set them apart. Probably stick with neutral and simple colors - white, grey etc. We need space for the traditional elements, including name, title, address, email/phone number. And we will be creating several from this template so it needs to be template that is easy to switch information in and out of.
Business
See description

```html
<!DOCTYPE html>
<html lang="en">
<head>
<meta charset="utf-8">
<title>Harborline Holdings – Business Card</title>
<link href="https://fonts.googleapis.com/css2?family=Open+Sans:wght@400;600;700;800&display=swap" rel="stylesheet">
<style>
  :root {
    --stage: #e9e6e1;
    --card-white: #ffffff;
    --card-black: #2a2a2a;
    --ink: #1b1b1b;
    --gold: #b39b72;
    --text: #222222;
    --white: #ffffff;
  }
  * { box-sizing: border-box; margin: 0; padding: 0; }
  html, body {
    width: 1200px; height: 900px; overflow: hidden;
    background: var(--stage);
    font-family: "Open Sans", Arial, sans-serif;
  }
  .canvas { position: relative; width: 1200px; height: 900px; }

  .card {
    position: absolute;
    width: 600px; height: 343px;
    overflow: hidden;
    box-shadow: 0 10px 24px rgba(0,0,0,0.18);
  }

  /* Back side */
  .card-back { left: 540px; top: 60px; background: var(--card-black); }
  .card-back .wordmark { color: var(--white); }

  /* Front side */
  .card-front { left: 60px; top: 480px; background: var(--card-white); }
  .card-front .wordmark { color: var(--ink); }

  .wordmark {
    position: absolute;
    text-align: center;
    font-family: "Open Sans", Arial, sans-serif;
    font-weight: 800;
    line-height: 1;
    text-transform: uppercase;
  }
  .wordmark .primary { display: block; letter-spacing: 1px; }
  .wordmark .secondary { display: block; letter-spacing: 12px; margin-top: 8px; }

  .card-back .wordmark { left: 0; right: 0; top: 118px; }
  .card-back .wordmark .primary { font-size: 56px; }
  .card-back .wordmark .secondary { font-size: 28px; padding-left: 12px; }

  .card-front .wordmark { left: 290px; width: 290px; top: 132px; }
  .card-front .wordmark .primary { font-size: 34px; }
  .card-front .wordmark .secondary { font-size: 18px; letter-spacing: 8px; padding-left: 8px; }

  .corner-tab { position: absolute; left: 22px; top: 22px; }

  .identity { position: absolute; left: 80px; top: 24px; }
  .identity .name { color: var(--gold); font-weight: 700; font-size: 21px; line-height: 1.2; }
  .identity .title { color: var(--text); font-size: 13px; }

  .address {
    position: absolute; left: 40px; top: 128px;
    font-size: 14px; line-height: 1.4; color: var(--text);
  }
  .contact {
    position: absolute; left: 22px; top: 176px;
    list-style: none; font-size: 14px; line-height: 1.45; color: var(--text);
  }
  .contact li { display: flex; align-items: center; gap: 8px; }
  .contact svg { width: 11px; height: 11px; fill: var(--gold); flex: none; }

  .bands { position: absolute; left: 0; top: 0; }
</style>
</head>
<body>
<main class="canvas">

  <section class="card card-back" aria-label="Business card, back">
    <div class="wordmark">
      <span class="primary">Harborline</span>
      <span class="secondary">Holdings</span>
    </div>
  </section>

  <section class="card card-front" aria-label="Business card, front">
    <svg class="bands" width="600" height="343" viewBox="0 0 600 343" aria-hidden="true">
      <polygon points="0,258 300,258 288,282 0,282" fill="var(--gold)"/>
      <polygon points="302,274 600,274 600,322 280,322" fill="var(--ink)"/>
    </svg>

    <svg class="corner-tab" width="44" height="34" viewBox="0 0 44 34" aria-hidden="true">
      <polygon points="26,0 44,0 40,34 0,34" fill="var(--ink)"/>
    </svg>

    <div class="identity">
      <p class="name">Marcus Ellery</p>
      <p class="title">Managing Director</p>
    </div>

    <p class="address">12345, Address Goes Here<br>Country Name, 123456.</p>

    <ul class="contact">
      <li>
        <svg viewBox="0 0 24 24"><path d="M6.6 10.8a15.1 15.1 0 0 0 6.6 6.6l2.2-2.2a1 1 0 0 1 1-.25 11.4 11.4 0 0 0 3.6.57 1 1 0 0 1 1 1V20a1 1 0 0 1-1 1A17 17 0 0 1 3 4a1 1 0 0 1 1-1h3.5a1 1 0 0 1 1 1c0 1.25.2 2.45.57 3.57a1 1 0 0 1-.25 1z"/></svg>
        <span>044-123 456 789</span>
      </li>
      <li>
        <svg viewBox="0 0 24 24"><path d="M2 5h20v14H2z M2 5l10 8 10-8" stroke="var(--white)" stroke-width="1.5"/></svg>
        <span>hello@yourdomain.com</span>
      </li>
      <li>
        <svg viewBox="0 0 24 24"><path d="M10 14a5 5 0 0 0 7 0l3-3a5 5 0 0 0-7-7l-1 1 1.5 1.5 1-1a3 3 0 0 1 4 4l-3 3a3 3 0 0 1-4 0zM14 10a5 5 0 0 0-7 0l-3 3a5 5 0 0 0 7 7l1-1-1.5-1.5-1 1a3 3 0 0 1-4-4l3-3a3 3 0 0 1 4 0z"/></svg>
        <span>www.yourdomain.com</span>
      </li>
    </ul>

    <div class="wordmark">
      <span class="primary">Harborline</span>
      <span class="secondary">Holdings</span>
    </div>
  </section>

</main>
</body>
</html>
```